PENNIMARTEL & PENNIMARTEL,LLP NEEDS A NEW LETTERHEAD DESIGN

a conservative yet contemporary layout befitting a long established
firm, consistent with the times, some form of logo so it catches ones attention, and is
admirable, but portrays integrity
Updates

I would like to approve #22066987 Please advise how to do this as it’s confusing on the site so I can approve payment for the designer

Target Market(s)

real estate investors and building management people

Industry/Entity Type

Law Firm

Font styles to use
Serif

Colors

Designer to choose colors to be used in the design.

Requirements
Must have
• some form of conservative logo

```html
<!DOCTYPE html>
<html lang="en">
<head>
<meta charset="utf-8">
<title>Pennimartel &amp; Pennimartel LLP — Letterhead</title>
<link rel="stylesheet" href="https://fonts.googleapis.com/css2?family=Cinzel:wght@400;500&family=Heebo:wght@300;400&display=swap">
<style>
  :root {
    --backdrop: #c9cacf;
    --paper: #f3f3f3;
    --gold: #d9a432;
    --ink: #4f5052;
    --ink-soft: #626366;
    --rule: #9a9b9e;
  }
  * { box-sizing: border-box; margin: 0; padding: 0; }
  html, body { width: 1200px; height: 1166px; overflow: hidden; }
  body {
    background: var(--backdrop);
    font-family: "Heebo", "Helvetica Neue", Arial, sans-serif;
    font-weight: 300;
    color: var(--ink);
  }
  .letterhead {
    position: absolute;
    left: 175px;
    top: 33px;
    width: 850px;
    height: 1100px;
    background: var(--paper);
  }
  .brand {
    position: absolute;
    left: 76px;
    top: 62px;
    display: flex;
    align-items: center;
    gap: 18px;
  }
  .brand-mark { width: 66px; height: 66px; flex: none; }
  .brand-text { border-top: 0; }
  .firm-name {
    font-family: "Cinzel", Georgia, serif;
    font-weight: 500;
    font-size: 22px;
    letter-spacing: 0.2px;
    color: var(--ink);
    padding-bottom: 5px;
    border-bottom: 1px solid var(--rule);
    white-space: nowrap;
  }
  .firm-tagline {
    font-family: "Cinzel", Georgia, serif;
    font-weight: 400;
    font-size: 10.5px;
    letter-spacing: 5.4px;
    color: var(--ink-soft);
    margin-top: 8px;
    white-space: nowrap;
  }
  .contact {
    position: absolute;
    right: 76px;
    top: 70px;
    text-align: right;
    font-size: 11px;
    line-height: 17px;
    color: var(--ink-soft);
  }
  .contact .phones { margin-top: 17px; }
  .contact .label { color: var(--gold); }
  .recipient {
    position: absolute;
    left: 76px;
    top: 265px;
    font-size: 12px;
    line-height: 14.8px;
    color: var(--ink-soft);
  }
  .letter-body {
    position: absolute;
    left: 76px;
    top: 391px;
    width: 698px;
    font-size: 11.9px;
    line-height: 14.7px;
    color: var(--ink-soft);
    letter-spacing: -0.15px;
  }
  .letter-body p { text-align: justify; margin-bottom: 14.5px; }
  .signoff {
    position: absolute;
    left: 76px;
    top: 799px;
    font-size: 12px;
    line-height: 14.8px;
    color: var(--ink-soft);
  }
  .signature {
    width: 140px;
    height: 58px;
    margin: 22px 0 20px;
    background: linear-gradient(90deg, #e6e6e6, #dcdcdc);
  }
  .footer {
    position: absolute;
    left: 76px;
    right: 76px;
    top: 1040px;
    display: flex;
    align-items: center;
    gap: 16px;
    font-size: 11px;
    color: var(--ink-soft);
  }
  .footer-rule { flex: 1; height: 1px; background: var(--rule); }
  .footer .sep { color: var(--gold); margin: 0 8px; }
</style>
</head>
<body>
  <main class="letterhead">
    <header class="brand">
      <svg class="brand-mark" viewBox="0 0 66 66" aria-hidden="true">
        <circle cx="33" cy="33" r="31" fill="none" stroke="var(--gold)" stroke-width="2"/>
      </svg>
      <div class="brand-text">
        <div class="firm-name">Pennimartel &amp; Pennimartel LLP</div>
        <div class="firm-tagline">Attorneys and Counselors at Law</div>
      </div>
    </header>

    <address class="contact" style="font-style:normal">
      <div>41 Ashcombe Street Suite 210</div>
      <div>Eastbrook, New York 11290</div>
      <div class="phones">
        <div><span class="label">T:</span> (555)-310-4412</div>
        <div><span class="label">F:</span> (555)-310-4418</div>
      </div>
    </address>

    <address class="recipient" style="font-style:normal">
      Mr. Lionel Farrowby<br>
      President and CEO<br>
      VerdaCore LLC.<br>
      880 Halvern Avenue, Suite 2100<br>
      New York, NY 10087
    </address>

    <section class="letter-body">
      <p>Dear Mr. Farrowby:</p>
      <p>As Chairperson of the Corporate Conscience Campaign - Helping the Homeless in New York, I am writing this to thank you personally for your company's support in last month's fund-raising effort.</p>
      <p>As I indicated when we spoke on the phone two weeks ago, the campaign was considered a resounding success, raising a total of $1.65 million to-date, significantly exceeding our target of $1 million. Some donations are still trickling in, so we could end up close to a total of $2 million.</p>
      <p>VerdaCore was an influential leader throughout the entire three-month campaign. In fact, we couldn't have succeeded without the generous support of your company, both financially, and through your organizational and administrative assistance. Your Team Leader, Marisol Quentin was particularly impressive, going above and beyond what we could have expected of someone performing as a volunteer while continuing on with her day-to-day duties. Please convey my special thanks to Marisol.</p>
      <p>I would also ask you to convey my sincere thanks and congratulations to all of those other people in your company who contributed in any way to the Helping the Homeless Campaign. Please tell them that the sum of their contributions resulted in a major success that they should all be proud of taking part in.</p>
      <p>I believe that the 27 companies that participated in this effort have set a new standard for social responsibility in this community, and have set a powerful example that will inspire other companies and organizations to do the same.</p>
      <p>I look forward to seeing you at the Mayor's special thank you reception next month.</p>
    </section>

    <section class="signoff">
      <div>Yours sincerely,</div>
      <div class="signature" role="img" aria-label="Handwritten signature of Edmund Harlowe"></div>
      <div>Edmund Harlowe</div>
      <div>Fundraising Chair</div>
    </section>

    <footer class="footer">
      <div class="footer-rule"></div>
      <div>info@pennimartel-law.com<span class="sep">/</span>www.pennimartel-law.com</div>
    </footer>
  </main>
</body>
</html>
```